High-end residential home builder needs a business card design

We need a new business card design for a small residential construction company based in Boise, Idaho. We specialize in building custom high-end homes and remodels, with a focus on great design and craftsmanship.

We would like to use our current logo, but open to new color suggestions.
Just looking for a clean, sharp, modern design that looks high-end.

Target Market(s)

Upscale clientele

Industry/Entity Type

Contractor

Contact Information for Business Card

Company: Stonefield Custom Builders
Name: Marcus Tilley
Phone number: 208 367 4120
Email: MarcusTilleySCB@mailbox-example.com
Website: Stonefieldcustombuilders-example.com

Font styles to use
Serif
Sans Serif

Requirements
Must have
• Company Logo
Company name
My name
My phone number
My email
Company website
Nice to have
• I have attached a few photos of cards that I really like.

```html
<!DOCTYPE html>
<html lang="en">
<head>
<meta charset="utf-8">
<title>Stonefield Custom Builders – Business Card</title>
<link rel="stylesheet" href="https://fonts.googleapis.com/css2?family=EB+Garamond:wght@400&family=Raleway:wght@700&display=swap">
<style>
  :root {
    --ink: #231815;
    --accent: #e8890c;
    --paper: #ffffff;
    --band: #efefed;
  }
  * { margin: 0; padding: 0; box-sizing: border-box; }
  html, body {
    width: 1200px;
    height: 686px;
    overflow: hidden;
    background: var(--paper);
  }
  .card {
    position: relative;
    width: 1200px;
    height: 686px;
    background: var(--paper);
    color: var(--ink);
  }
  .brand-mark {
    position: absolute;
    left: 184px;
    top: 140px;
    width: 180px;
    height: 180px;
    border: 3px solid var(--accent);
  }
  .brand-name {
    position: absolute;
    left: 0;
    width: 548px;
    text-align: center;
    font-family: "Raleway", sans-serif;
    font-weight: 700;
    color: var(--ink);
    text-transform: uppercase;
    line-height: 1;
  }
  .brand-name--main {
    top: 396px;
    font-size: 38px;
    letter-spacing: 0.2em;
  }
  .brand-name--sub {
    top: 462px;
    font-size: 22px;
    letter-spacing: 0.22em;
  }
  .person-name {
    position: absolute;
    left: 575px;
    top: 150px;
    font-family: "EB Garamond", serif;
    font-weight: 400;
    font-size: 56px;
    line-height: 70px;
    letter-spacing: 0.2em;
    text-transform: uppercase;
  }
  .contact {
    position: absolute;
    left: 575px;
    top: 398px;
    font-family: "EB Garamond", serif;
    font-size: 33px;
    line-height: 58px;
    list-style: none;
  }
  .website-band {
    position: absolute;
    left: 0;
    top: 568px;
    width: 1200px;
    height: 118px;
    background: var(--band);
    display: flex;
    align-items: center;
    justify-content: center;
  }
  .website {
    font-family: "EB Garamond", serif;
    font-size: 42px;
    letter-spacing: 0.07em;
    color: var(--ink);
  }
</style>
</head>
<body>
  <main class="card">
    <div class="brand-mark"></div>
    <div class="brand-name brand-name--main">Stonefield</div>
    <div class="brand-name brand-name--sub">Custom Builders</div>

    <h1 class="person-name">Marcus<br>Tilley</h1>

    <ul class="contact">
      <li class="contact-phone">Phone: (208) 367-4120</li>
      <li class="contact-email">MarcusTilleySCB@mailbox-example.com</li>
    </ul>

    <footer class="website-band">
      <span class="website">stonefieldcustombuilders-example.com</span>
    </footer>
  </main>
</body>
</html>
```